Business Card

I need a business card that is fresh, styling and reflects my heart centered healing business while still maintaining full professionalism as I have an my evidence-based practice. I am a Naturopath and a Shiatsu Massage Therapist.
Below are my existing logo (file 1) and an inspiration image (file 2) that reflects the colours and style I would like to express to my card (blues greens). I especially like that tree wallpaper.

Information for the card:
Tessa Gorrinde
BHSc. (Nat) m.QRPC
Naturopath
Herbalist
Nutritionist
Shiatsu Therapist
Wellness Counsellor

41 Dovertan St South Fremantle
www.tessagorrinde.com.au
tessa@tessagorrinde.com.au

NOte: I've removed part of the brief, in that I've changed my mind about the back of the card being a '5 treatments and get sixth one free" I'd rather have this on a separate card. So please do not include this in your designs.
Updates

Hi Guys, I've taken the '5 session get the sixth free' part out of the brief. Also, I've added the info to go on the business card into the brief.

Thanks and happy designing
Tes

I've just uploaded a high res better quality version of the hand logo. Thanks Lovlies. 

Target Market(s)

I am targeting western women of ages 25 - 40 in preconception care, sugar addiction therapy, and wellness coaching. I want must card to be vibrant, positive and current.

Industry/Entity Type

Business

Requirements
Must have
• Please include my hand image logo

```html
<!DOCTYPE html>
<html lang="en">
<head>
<meta charset="utf-8">
<title>Tessa Gorrinde – Business Card</title>
<link rel="stylesheet" href="https://fonts.googleapis.com/css2?family=Ubuntu:wght@300;400;500&display=swap">
<style>
  :root {
    --backdrop: #b6b5af;
    --card-white: #ffffff;
    --mint: #9fd6c9;
    --mint-soft: #d9f0ea;
    --ink-grey: #4e4e4e;
    --royal: #2b3b93;
    --royal-light: #3a4ca6;
    --white: #ffffff;
  }
  * { margin: 0; padding: 0; box-sizing: border-box; }
  html, body {
    width: 1200px;
    height: 984px;
    overflow: hidden;
    background: var(--backdrop);
    font-family: "Ubuntu", sans-serif;
  }
  .canvas {
    position: relative;
    width: 1200px;
    height: 984px;
    display: flex;
    justify-content: center;
    align-items: center;
    gap: 80px;
  }
  .card {
    position: relative;
    width: 380px;
    height: 560px;
    border-radius: 24px;
    overflow: hidden;
    box-shadow: 0 6px 14px rgba(0,0,0,0.18);
  }

  /* Contact side */
  .card--contact { background: var(--card-white); }
  .contact__pattern {
    position: absolute;
    inset: 0 0 auto 0;
    height: 330px;
    background: linear-gradient(180deg, var(--mint) 0%, var(--mint-soft) 75%, var(--card-white) 100%);
  }
  .contact__details {
    position: absolute;
    left: 0;
    right: 0;
    top: 400px;
    text-align: center;
    color: var(--ink-grey);
    font-size: 19px;
    font-weight: 400;
    line-height: 1.45;
  }

  /* Identity side */
  .card--identity { background: var(--royal); color: var(--white); }
  .identity__pattern {
    position: absolute;
    inset: 0;
    background: radial-gradient(circle at 50% 30%, var(--royal-light) 0%, var(--royal) 70%);
  }
  .identity__mark {
    position: absolute;
    top: 70px;
    left: 0;
    right: 0;
    display: flex;
    flex-direction: column;
    align-items: center;
    gap: 14px;
  }
  .identity__mark-dot {
    width: 110px;
    height: 110px;
    border-radius: 50%;
    background: var(--white);
  }
  .identity__mark-name {
    font-size: 20px;
    font-weight: 400;
    color: var(--white);
  }
  .identity__name {
    position: absolute;
    top: 355px;
    left: 0;
    right: 0;
    text-align: center;
    font-size: 38px;
    font-weight: 300;
  }
  .identity__credentials {
    position: absolute;
    top: 420px;
    left: 0;
    right: 0;
    text-align: center;
    font-size: 15px;
    font-weight: 500;
    line-height: 1.55;
  }
</style>
</head>
<body>
  <main class="canvas">
    <section class="card card--contact">
      <div class="contact__pattern" role="img" aria-label="Mint floral hand-motif wallpaper pattern"></div>
      <div class="contact__details">
        <p>41 Dovertan St South Fremantle</p>
        <p>www.tessagorrinde.com.au</p>
        <p>tessa@tessagorrinde.com.au</p>
      </div>
    </section>

    <section class="card card--identity">
      <div class="identity__pattern" role="img" aria-label="Faint blue floral hand-motif wallpaper pattern"></div>
      <div class="identity__mark">
        <span class="identity__mark-dot"></span>
        <span class="identity__mark-name">Tessa Gorrinde</span>
      </div>
      <h1 class="identity__name">Tessa Gorrinde</h1>
      <div class="identity__credentials">
        <p>BHSc. (Nat) m.QRPC • Naturopath</p>
        <p>Herbalist • Nutritionist</p>
        <p>Shiatsu Therapist • Wellness Counsellor</p>
      </div>
    </section>
  </main>
</body>
</html>
```